Crumbwell Courier The Next Generation

we have a website www.crumbwellcourier.ae which needs a complete graphical overhaul.
We are a bakery in Dubai, producing artisan breads and related products. Also salads and sandwiches. All fresh, all handmade, best quality.
We'd like to have something that looks fresh, modern, nice colours (no dark colours). Trendy but still transporting the feeling of the "good ol' bakery).
Our customers are expats, mostly english speakers. But we'd like to attract more different nationalities!
Also, customers are individuals and also companies (offices, airlines, yacht charters...) The third section are coffee shops, restaurants, hotels....
We have also an online shop. This is a MUST and can be optimised.
We'd like to stick with wordpress and woocommerce.
It MUST be responsive and easy to navigate on mobile devices. 60% of our customers order on mobile phones... browsing is even more.

Bakery

```html
<!DOCTYPE html>
<html lang="en">
<head>
<meta charset="utf-8">
<title>Crumbwell Courier – Artisan Bakery</title>
<link rel="stylesheet" href="https://fonts.googleapis.com/css2?family=Roboto:wght@300;400;500;700&display=swap">
<style>
:root{
  --green:#3d5622;
  --green-light:#4f6e2c;
  --ink:#333;
  --muted:#666;
  --line:#e2e2e2;
  --band:#f1f1f1;
  --white:#fff;
}
*{box-sizing:border-box;margin:0;padding:0}
html,body{width:1200px;height:2571px;overflow:hidden}
body{position:relative;background:var(--white);font-family:'Roboto',Arial,sans-serif;color:var(--ink)}
.abs{position:absolute}
/* header */
.brand{left:111px;top:38px;height:40px;display:flex;align-items:center;gap:12px;color:var(--green);font-weight:500;font-size:22px;white-space:nowrap}
.brand i{display:block;width:22px;height:22px;background:var(--green)}
.contact{display:flex;align-items:center;gap:14px;top:36px}
.contact .ring{width:42px;height:42px;border:1px solid #ccc;border-radius:50%;display:flex;align-items:center;justify-content:center}
.contact b{display:block;font-weight:400;font-size:15px;color:var(--ink)}
.contact span{font-size:12.5px;color:var(--muted)}
.tools{left:1004px;top:44px;display:flex;gap:22px;align-items:center}
.badge{position:absolute;width:16px;height:16px;border-radius:50%;background:#c0641a;color:#fff;font-size:10px;display:flex;align-items:center;justify-content:center}
.nav{left:0;top:117px;width:1200px;height:41px;background:var(--band)}
.nav ul{list-style:none;display:flex;justify-content:space-between;width:976px;margin-left:111px;height:41px;align-items:center}
.nav li{font-size:14.5px;text-transform:uppercase;color:#333;height:41px;line-height:41px;padding:0 18px}
.nav li.active{color:var(--green);border-bottom:2px solid var(--green);position:relative}
/* hero */
.tile{overflow:hidden}
.tile h2{position:absolute;left:18px;font-weight:400;color:#fff;font-size:40px}
.tile a{position:absolute;left:18px;color:#fff;font-weight:500;font-size:14.5px;text-decoration:none}
/* features */
.feature{top:658px;width:309px;height:88px;border:1px solid var(--line);display:flex;align-items:center;justify-content:center;gap:16px;font-size:20px;font-weight:500;color:#333;text-transform:uppercase}
/* about */
.about{left:0;top:789px;width:1200px;height:563px;background:linear-gradient(135deg,#4a4e2a,#5d4a2b 40%,#3e4a28 70%,#5a3e28);color:#fff;text-align:center}
.about h2{margin-top:52px;font-size:31px;font-weight:500}
.about p{width:960px;margin:0 auto;font-size:13.2px;line-height:1.55}
.partner{width:640px;height:76px;margin:22px auto 28px;background:#fff;padding:8px}
.partner div{border:2px solid var(--green);height:100%;display:flex;align-items:center;justify-content:center;color:#222;font-size:21px}
.partner span{color:var(--green)}
/* menu */
.menu-title{top:1406px;width:1200px;text-align:center;font-size:30px;font-weight:400;color:#222}
.tabs{top:1462px;left:0;width:1200px;height:38px;border-top:1px dotted #bbb;border-bottom:1px dotted #bbb;display:flex;justify-content:center;gap:54px;align-items:center;font-size:15px;color:#444}
.tabs .on{color:var(--green);font-weight:500}
.card{width:226px;height:241px;border:1px solid var(--line);background:#fff;text-align:center}
.card .ph{height:171px}
.card h3{font-weight:400;font-size:15.5px;margin-top:12px;color:#222}
.card p{font-size:13px;color:var(--green);margin-top:8px}
.card.hover{box-shadow:0 4px 10px rgba(0,0,0,.18)}
.card .add{position:absolute;left:35px;top:187px;width:156px;height:36px;background:var(--green);color:#fff;font-size:13.5px;display:flex;align-items:center;justify-content:center;gap:12px}
.more{left:537px;top:2081px;width:126px;height:34px;background:var(--green);color:#fff;font-size:13.5px;display:flex;align-items:center;justify-content:center;gap:7px}
/* footer */
.footer{left:0;top:2177px;width:1200px;height:346px;background:#efefef}
.footer h4{position:absolute;top:56px;font-size:20px;font-weight:400;color:#222}
.links{position:absolute;left:111px;top:92px;list-style:none;font-size:12px;line-height:25.6px;color:#333}
.map{position:absolute;left:278px;top:98px;width:505px;height:187px;background:linear-gradient(135deg,#e9e5dc,#dcd9cf 50%,#efe6c8);border:1px solid #d5d5d5}
.info{position:absolute;left:828px;font-size:12px;color:#333;line-height:18px;display:flex;gap:14px}
.social{position:absolute;top:269px;width:26px;height:26px;border:1px solid var(--green)}
.bar{left:0;top:2523px;width:1200px;height:48px;background:var(--green);color:#fff;font-size:13px;display:flex;align-items:center;justify-content:center}
</style>
</head>
<body>

<header>
  <div class="abs brand"><i></i>Crumbwell Courier</div>
  <div class="abs contact" style="left:530px">
    <div class="ring"><svg width="18" height="18" viewBox="0 0 24 24" fill="none" stroke="#666" stroke-width="1.6"><path d="M5 3h4l2 5-2.5 1.5a11 11 0 0 0 6 6L16 13l5 2v4a2 2 0 0 1-2 2A17 17 0 0 1 3 5a2 2 0 0 1 2-2z"/></svg></div>
    <div><b>Call us on</b><span>050 318 62 07</span></div>
  </div>
  <div class="abs contact" style="left:698px">
    <div class="ring"><svg width="18" height="14" viewBox="0 0 24 18" fill="none" stroke="#666" stroke-width="1.6"><rect x="1" y="1" width="22" height="16"/><path d="M1 1l11 9 11-9"/></svg></div>
    <div><b>Send your mail at</b><span>hello@crumbwellcourier.ae</span></div>
  </div>
  <div class="abs tools">
    <svg width="26" height="26" viewBox="0 0 24 24" fill="none" stroke="var(--green)" stroke-width="1.8"><circle cx="10" cy="10" r="7"/><path d="M15 15l7 7"/></svg>
    <div style="position:relative"><svg width="26" height="24" viewBox="0 0 24 22" fill="none" stroke="var(--green)" stroke-width="1.8"><path d="M1 2h4l3 12h12l2-8H7"/><circle cx="9" cy="19" r="1.6"/><circle cx="18" cy="19" r="1.6"/></svg><span class="badge" style="left:14px;top:-10px">0</span></div>
  </div>
  <nav class="abs nav"><ul>
    <li class="active">Welcome</li><li>Our Menu</li><li>Our Boxes</li><li>Great British Pies</li><li>Order and Delivery</li><li>Get in Touch</li>
  </ul></nav>
</header>

<section class="hero">
  <div class="abs tile" style="left:0;top:173px;width:763px;height:442px;background:linear-gradient(120deg,#5e4a3a,#8a6a48 40%,#b9803e 60%,#5b4636)" role="img" aria-label="Golden baguettes on a wooden table">
    <h2 style="top:34px;left:118px">Baguette</h2><a style="top:96px;left:125px">Add to Basket ➔</a>
  </div>
  <div class="abs tile" style="left:780px;top:173px;width:420px;height:214px;background:linear-gradient(120deg,#8b4a26,#c17a3e 50%,#a8382a)" role="img" aria-label="Mini quiches with tomato">
    <h2 style="top:2px;left:6px">Mini Quiche</h2><a style="top:63px;left:12px">Add to Basket ➔</a>
  </div>
  <div class="abs tile" style="left:780px;top:403px;width:420px;height:212px;background:linear-gradient(120deg,#3e5a78,#6c7e8c 45%,#c39a62 75%,#e0c49a)" role="img" aria-label="Basket of assorted bread rolls">
    <h2 style="top:2px;left:6px">Couples Box</h2><a style="top:60px;left:12px">Add to Basket ➔</a>
  </div>
</section>

<section class="features">
  <div class="abs feature" style="left:111px">
    <svg width="54" height="44" viewBox="0 0 54 44" fill="var(--green)"><path d="M12 14a15 12 0 0 1 30 0z"/><path d="M2 18h50l-6 22H8z"/></svg>Fresh</div>
  <div class="abs feature" style="left:446px">
    <svg width="44" height="50" viewBox="0 0 44 50" fill="none" stroke="var(--green)" stroke-width="3"><path d="M12 26V8a3 3 0 0 1 6 0v14V4a3 3 0 0 1 6 0v18V7a3 3 0 0 1 6 0v17-11a3 3 0 0 1 6 0v18c0 10-6 16-14 16-6 0-10-4-14-10l-6-9a3 3 0 0 1 5-3z"/></svg>Handmade</div>
  <div class="abs feature" style="left:780px">
    <svg width="50" height="50" viewBox="0 0 50 50"><path fill="var(--green)" d="M25 2l6 5 8-1 2 8 7 4-3 7 3 7-7 4-2 8-8-1-6 5-6-5-8 1-2-8-7-4 3-7-3-7 7-4 2-8 8 1z"/><path d="M15 25l7 7 13-14" fill="none" stroke="#fff" stroke-width="4"/></svg>Best Quality</div>
</section>

<section class="abs about" role="img" aria-label="Dimmed background photo of fresh salad ingredients">
  <h2>ABOUT US</h2>
  <p style="margin-top:22px">Are you searching for great bread? Maybe a mouth watering sandwich? Is your next party coming up and you need finger food? No, you're looking for this great British pie that arouses memories from home? Aha!! you have an event at the office and you need sandwich platters!</p>
  <div class="partner"><div>Then,&nbsp;<span>Crumbwell Courier</span>&nbsp;is your partner.</div></div>
  <p>In hectic times like this, many produce bread in a short period of time, adding additives to get a quick result. Not us. We are artisans. What does that mean? It means that every bread, sandwich or pie is carefully made by hand, and we take the time needed for our bread and pastry to develop the taste we're after. We develop our recipes so that we can deliver taste and quality. We're passionate about what we do and what we make!</p>
  <p style="margin-top:20px">If you're a pie lover, then you must try our British pies – from traditional to modern, down to earth or extravagant. You can have pies with meat, chicken or vegetables. We are constantly working on new recipes. Hey, we'll even try out any suggestions you might have for your ideal pie!</p>
  <p style="margin-top:20px">Are you an entertainer, looking for easy but delicious ways to cater for your guests?</p>
  <p style="margin-top:20px">Our finger foods are the formula 1 of party or event foods. From a simple triangle sandwich, a distinguished canapé, an exquisite mini burger, mouth watering mini pies or a cheese mini quiche, you've come to the right place. We cater small to large events or parties!</p>
  <p style="margin-top:20px">We deliver all over Dubai and, if you have the budget, even to the moon...</p>
</section>

<section class="menu">
  <h2 class="abs menu-title">OUR MENU</h2>
  <div class="abs tabs"><span>All</span><span class="on">Breads, baps and more</span><span>Snadwich Platters</span><span>Finger foods</span><span>Salads</span><span>Great British Pies</span></div>

  <div class="abs card" style="left:111px;top:1526px"><div class="ph" role="img" aria-label="Round focaccia" style="background:linear-gradient(135deg,#8a6a48,#c79a4e 50%,#6e5a48)"></div><h3>Focaccia</h3><p>3.50 AED - 12.00 AED</p></div>
  <div class="abs card hover" style="left:362px;top:1526px"><div class="ph" role="img" aria-label="Sliced white loaf" style="background:linear-gradient(135deg,#9aa0a4,#e8cf98 50%,#d9b676)"></div><div class="add">Add to Basket <svg width="20" height="18" viewBox="0 0 24 22" fill="none" stroke="#fff" stroke-width="1.8"><path d="M1 2h4l3 12h12l2-8H7"/><circle cx="9" cy="19" r="1.6"/><circle cx="18" cy="19" r="1.6"/></svg></div></div>
  <div class="abs card" style="left:612px;top:1526px"><div class="ph" role="img" aria-label="Cottage loaf" style="background:linear-gradient(135deg,#4e3e30,#d9c7a8 50%,#6a5440)"></div><h3>Cottage Loaf</h3><p>7.90 AED</p></div>
  <div class="abs card" style="left:862px;top:1526px"><div class="ph" role="img" aria-label="English sliced bread loaves" style="background:linear-gradient(135deg,#8a6a40,#e3b25e 50%,#c89040)"></div><h3>English Sliced</h3><p>9.50 AED</p></div>

  <div class="abs card" style="left:111px;top:1793px"><div class="ph" role="img" aria-label="Braided zopf bread" style="background:linear-gradient(135deg,#6e5a48,#c0702a 50%,#8a6a50)"></div><h3>Zopf</h3><p>9.90 AED</p></div>
  <div class="abs card" style="left:362px;top:1793px"><div class="ph" role="img" aria-label="Six floured baps" style="background:linear-gradient(135deg,#b8ad9c,#d9b88c 50%,#8e8070)"></div><h3>Baps (6 Pcs)</h3><p>10.00 AED - 16.00 AED</p></div>
  <div class="abs card" style="left:612px;top:1793px"><div class="ph" role="img" aria-label="Heart shaped braided bread" style="background:linear-gradient(135deg,#6e5038,#c8782e 50%,#7a5a40)"></div><h3>Valentine's Heart</h3><p>16.00 AED - 24.00 AED</p></div>
  <div class="abs card" style="left:862px;top:1793px"><div class="ph" role="img" aria-label="Dark malt bread loaves" style="background:linear-gradient(135deg,#5a4838,#9a6a44 50%,#4a3a2e)"></div><h3>Dark Malt Bread (2 Pcs)</h3><p>16.90 AED</p></div>

  <div class="abs more">View more <svg width="14" height="14" viewBox="0 0 14 14"><circle cx="7" cy="7" r="7" fill="#fff"/><path d="M4 7h5M7 4l3 3-3 3" stroke="var(--green)" stroke-width="1.6" fill="none"/></svg></div>
</section>

<footer class="abs footer">
  <h4 style="left:111px">Quick Link</h4>
  <ul class="links"><li>Our Menu</li><li>Our Boxes</li><li>Great British Pies</li><li>Order and Delivery</li><li>Get in Touch</li><li>Payment Terms</li><li>Terms and Conditions</li><li>Privacy</li></ul>
  <h4 style="left:278px">Our Location</h4>
  <div class="map" role="img" aria-label="Street map showing the bakery location"></div>
  <h4 style="left:828px">Contact Info</h4>
  <div class="info" style="top:93px"><svg width="16" height="16" viewBox="0 0 16 16" fill="none" stroke="#555"><path d="M1 3l4-2 6 2 4-2v12l-4 2-6-2-4 2z"/></svg><span>Crumbwell Courier Bakery – Al Karama<br>Palm Court Building, Shop 5<br>9th Street<br>Near Garden Square</span></div>
  <div class="info" style="top:180px"><svg width="16" height="16" viewBox="0 0 24 24" fill="none" stroke="#555" stroke-width="2"><path d="M5 3h4l2 5-2.5 1.5a11 11 0 0 0 6 6L16 13l5 2v4a2 2 0 0 1-2 2A17 17 0 0 1 3 5a2 2 0 0 1 2-2z"/></svg><span>04 271 58 30</span></div>
  <div class="info" style="top:222px"><svg width="16" height="16" viewBox="0 0 24 24" fill="none" stroke="#555" stroke-width="2"><path d="M5 3h4l2 5-2.5 1.5a11 11 0 0 0 6 6L16 13l5 2v4a2 2 0 0 1-2 2A17 17 0 0 1 3 5a2 2 0 0 1 2-2z"/></svg><span>050 318 62 07</span></div>
  <div class="social" style="left:828px;background:var(--green)"></div>
  <div class="social" style="left:874px"></div>
  <div class="social" style="left:1058px;background:var(--green);display:flex;align-items:center;justify-content:center"><svg width="12" height="8" viewBox="0 0 12 8"><path d="M1 7l5-5 5 5" stroke="#fff" stroke-width="2" fill="none"/></svg></div>
</footer>
<div class="abs bar">Crumbwell Courier © 2017 &nbsp;|&nbsp; All Rights Reserved.</div>

</body>
</html>
```